RidgeHornSupply.com

I need a new webdesign for a company in the San Jose/SF Bay area that showcases the financial benefits of buying used band instruments for junior high students.This would be opposed to the current and costly option of renting cheap quality instruments from the 2 or 3 local music stores that charge a monthly fee that over the years charges the buyer 3 or 4x over..
Instruments: focus in on Alto Sax, Trumpet, Flute, Clarinet, Trombone, Tenor Sax, Baritone
Target middle schools are Kestrelwood Middle School and Harlow Middle School in San Jose, CA. Both have award winning band programs.
Files attached may or may not be important.
Tabs Needed and funtional
Contact
Shopping Cart
Select Instrument
Checkout
Add to Cart, etc.
Instuments
quantity, etc.
trade in your instrument/sell your instrument
ability to add or take away new instruments for sale. including pictures
Additional questions or info, feel free to ask
Hi Designers,
Project Deadline Extended
Reason: In the next week you will be receiving specific content that will be required to be had on the website.
New desigins are still welcome. Please continue to contact me if you have questions about your individual designs.
Thanks!
Ridge Horn

```html
<!DOCTYPE html>
<html lang="en">
<head>
<meta charset="utf-8">
<title>Ridge Horn Instruments</title>
<link href="https://fonts.googleapis.com/css2?family=Fredoka:wght@500;600&family=Arimo:wght@400;700&display=swap" rel="stylesheet">
<style>
:root{
  --red:#b82323;
  --red-dark:#9c1c1c;
  --red-soft:#c85a5a;
  --pink:#f6dada;
  --bar:#2b2b2b;
  --bar-line:#3a3a3a;
  --tile:#efefef;
  --text:#5a5a5a;
  --heading:#444;
  --white:#fff;
}
*{box-sizing:border-box;margin:0;padding:0}
html,body{width:969px;height:1200px;overflow:hidden;background:var(--white)}
.page{position:relative;width:1200px;height:1486px;transform:scale(.8075);transform-origin:0 0;font-family:"Arimo",Arial,sans-serif;color:var(--text)}
.abs{position:absolute}
.display{font-family:"Fredoka","Arial Rounded MT Bold",sans-serif;font-weight:600}

/* top bar */
.topbar{left:0;top:0;width:1200px;height:36px;background:var(--bar)}
.tool{position:absolute;top:0;width:37px;height:36px;border-left:1px solid var(--bar-line);display:flex;align-items:center;justify-content:center}
.tool svg{width:12px;height:12px;fill:#bbb}
.tool.active{background:#111}
.tool.active svg{fill:#fff}

/* header */
.header{left:0;top:36px;width:1200px;height:100px;background:var(--red)}
.logo{left:173px;top:38px;font-size:21px;letter-spacing:1.5px;color:var(--white)}
.nav{left:540px;top:45px;display:flex;gap:18px;font-size:11px;color:var(--white)}
.nav .current{font-weight:700}
.cart{left:904px;top:32px;width:124px;height:35px;background:var(--red-dark);display:flex;align-items:center;font-size:11px;font-weight:700;color:var(--white)}
.cart .icon{width:36px;height:35px;display:flex;align-items:center;justify-content:center;border-right:1px solid #8a1818;margin-right:11px}

/* hero */
.hero{left:0;top:136px;width:1200px;height:384px;background:linear-gradient(100deg,#7d1a1a,#b8403a 30%,#a8323a 55%,#c04a45 75%,#8b2a2a)}
.hero-title{left:0;top:196px;width:1200px;text-align:center;font-size:35px;color:var(--white);text-shadow:0 2px 4px rgba(0,0,0,.5)}
.hero-sub{left:290px;top:256px;width:620px;text-align:center;font-size:15px;font-weight:700;line-height:18px;color:var(--white);text-shadow:0 1px 3px rgba(0,0,0,.6)}
.prev,.next{top:322px;width:70px;height:62px;display:flex;align-items:center;justify-content:center}
.prev{left:172px;background:rgba(60,10,10,.6)}
.next{left:242px;background:var(--pink)}
.dots{left:544px;top:350px;display:flex;gap:5px}
.dots span{width:11px;height:11px;border-radius:50%;background:rgba(255,255,255,.45)}
.dots span.on{background:transparent;border:2px solid var(--white)}

/* welcome */
.welcome-title{left:176px;top:566px;font-size:27px;color:var(--red)}
.welcome-copy{left:177px;top:614px;width:552px;font-size:9px;line-height:11.2px;color:var(--text)}
.welcome-copy p{margin-bottom:9px}

/* news */
.news{left:750px;top:549px;width:272px;height:188px;background:var(--tile)}
.news h2{position:absolute;left:12px;top:18px;font-size:21px;color:var(--red)}
.news-item{position:absolute;left:0;width:272px;height:62px;display:flex;gap:6px;padding:8px 6px 0 10px}
.news-item.raised{background:#f5f5f5;box-shadow:0 1px 4px rgba(0,0,0,.2)}
.news-thumb{width:73px;height:49px;flex:none;background:linear-gradient(135deg,#c44,#e9a0a0)}
.news-thumb.alt{background:linear-gradient(135deg,#e8d6a0,#c45a3a)}
.news-item .t{font-size:9px;color:#444;margin-bottom:9px}
.news-item .d{font-size:9px;line-height:11px;color:#666}

.rule{left:170px;top:764px;width:860px;height:1px;background:#e3e3e3}

/* categories */
.cat-title{left:0;top:790px;width:1200px;text-align:center;font-size:21px;color:var(--red)}
.tile{position:absolute;width:162px;height:170px;background:var(--tile)}
.tile .pic{position:absolute;left:31px;top:18px;width:100px;height:110px;border-radius:6px;background:linear-gradient(160deg,#d9c48a,#9a8a6a)}
.tile .pic.silver{background:linear-gradient(160deg,#d8d8d8,#8a8a8a)}
.tile .pic.dark{background:linear-gradient(160deg,#6a6a6a,#2a2a2a)}
.tile .name{position:absolute;left:0;bottom:4px;width:162px;text-align:center;font-size:16px;color:var(--heading);font-family:"Fredoka",sans-serif;font-weight:500}
.tile.active{background:var(--red-soft);height:172px;width:164px;box-shadow:0 1px 5px rgba(0,0,0,.25)}
.tile.active .label{position:absolute;left:0;top:86px;width:164px;text-align:center;color:var(--white)}
.tile.active .label b{display:block;font-size:15px;font-family:"Fredoka",sans-serif;font-weight:600;letter-spacing:.5px}
.tile.active .label small{font-size:8px;font-family:"Fredoka",sans-serif;font-weight:600}

/* services band */
.band{left:0;top:1217px;width:1200px;height:172px;background:var(--red)}
.card{position:absolute;top:1240px;width:163px;height:163px;background:#f1f1f1;box-shadow:0 1px 3px rgba(0,0,0,.2)}
.card h3{position:absolute;left:8px;top:13px;width:150px;font-size:12px;line-height:15px;color:var(--heading);font-family:"Fredoka",sans-serif;font-weight:500}
.card .photo{position:absolute;left:7px;top:57px;width:150px;height:100px;background:linear-gradient(160deg,#c93a3a,#8a2020 60%,#5e7a3a)}
.card.active h3{color:var(--red)}
.card.active .photo{background:var(--red-soft);display:flex;align-items:center;justify-content:center}
.band-arrow{top:1296px;width:35px;height:31px;display:flex;align-items:center;justify-content:center}
.band-arrow.left{left:129px;background:var(--pink)}
.band-arrow.right{left:1036px;background:var(--red-dark)}

/* footer */
.copy{left:185px;top:1440px;font-size:9px;color:#555}
.social{left:897px;top:1432px;display:flex;gap:7px}
.social span{width:27px;height:27px;border-radius:50%;background:var(--red-soft)}
.social span:nth-child(even){background:var(--heading)}
</style>
</head>
<body>
<div class="page">

  <div class="abs topbar">
    <div class="tool" style="left:172px"><svg viewBox="0 0 12 12"><path d="M6 11 1 6a3 3 0 0 1 5-4 3 3 0 0 1 5 4z"/></svg></div>
    <div class="tool" style="left:209px"><svg viewBox="0 0 12 12"><circle cx="6" cy="3.5" r="2.5"/><path d="M1 11a5 4 0 0 1 10 0z"/></svg></div>
    <div class="tool" style="left:246px"><svg viewBox="0 0 12 12"><path d="M1 2h6v1H2v7h7V6h1v5H1zM9 1l2 2-5 5H4V6z"/></svg></div>
    <div class="tool" style="left:284px"><svg viewBox="0 0 12 12"><path d="M3 5V4a3 3 0 0 1 6 0v1h1v6H2V5zm1.5 0h3V4a1.5 1.5 0 0 0-3 0z"/></svg></div>
    <div class="tool active" style="left:321px"><svg viewBox="0 0 12 12"><circle cx="9" cy="2.5" r="2"/><circle cx="3" cy="6" r="2"/><circle cx="9" cy="9.5" r="2"/><path d="M3 6 9 2.5M3 6l6 3.5" stroke="#fff" stroke-width="1"/></svg></div>
    <div class="tool" style="left:955px"><svg viewBox="0 0 12 12"><path d="M3 1 5 3.5 4 5a6 6 0 0 0 3 3l1.5-1L11 9l-1.5 2C5 11 1 7 1 2.5z"/></svg></div>
    <div class="tool" style="left:992px;border-right:1px solid var(--bar-line)"><svg viewBox="0 0 12 12"><circle cx="5" cy="5" r="3.5" fill="none" stroke="#bbb" stroke-width="1.5"/><path d="m7.5 7.5 3 3" stroke="#bbb" stroke-width="1.8"/></svg></div>
  </div>

  <header class="abs header">
    <div class="abs logo display">RIDGE HORN INSTRUMENTS</div>
    <nav class="abs nav">
      <span class="current">HOME</span><span>INSTRUMENTS</span><span>TRADE IN</span><span>SELL OUT</span><span>CONTACT</span>
    </nav>
    <div class="abs cart">
      <span class="icon"><svg width="15" height="12" viewBox="0 0 15 12"><path d="M0 1h3l2 7h8l2-5H4" fill="none" stroke="#fff" stroke-width="1.5"/><circle cx="6" cy="10.5" r="1.2" fill="#fff"/><circle cx="12" cy="10.5" r="1.2" fill="#fff"/></svg></span>
      Cart: (empty)
    </div>
  </header>

  <section class="abs hero" role="img" aria-label="Marching band in red jackets playing saxophones in a packed stadium">
    <h1 class="abs hero-title display">LOREM IPSUM DOLOR SIT AMET,</h1>
    <p class="abs hero-sub">Consectetuer adipiscing elit, sed diam nonummy nibh euismod tincidunt ut laoreet dolore magna aliquam erat volutpat.</p>
    <div class="abs prev"><svg width="24" height="18" viewBox="0 0 24 18"><path d="M0 9 10 0v6h14v6H10v6z" fill="#ddd"/></svg></div>
    <div class="abs next"><svg width="24" height="18" viewBox="0 0 24 18"><path d="M24 9 14 0v6H0v6h14v6z" fill="var(--red)"/></svg></div>
    <div class="abs dots"><span></span><span></span><span class="on"></span><span></span><span></span><span></span><span></span></div>
  </section>

  <h2 class="abs welcome-title display">Welcome To Ridge Horn Instruments</h2>
  <div class="abs welcome-copy">
    <p>We show you financial benefits of buying used band instruments for junior high students.This would be opposed to the current and costly option of renting cheap quality instruments from the 2 or 3 local music stores that charge a monthly fee that over the years charges the buyer 3 or 4x over..</p>
    <p>Ut wisi enim ad minim veniam, quis nostrud exerci tation ullamcorper suscipit lobortis nisl ut aliquip ex ea commodo consequat. Duis autem vel eum iriure dolor in hendrerit in vulputate velit esse molestie consequat, vel illum dolore eu feugiat nulla facilisis at vero eros et accumsan et iusto odio dignissim qui blandit praesent luptatum zzril delenit augue duis dolore te feugait nulla facilisi.</p>
    <p>Scipit lobortis nisl ut aliquip ex ea commodo consequat. Duis autem vel eum iriure dolor in hendrerit in vulputate velit esse molestie consequat, vel illum dolore eu feugiat nulla facilisis at vero eros et accumsan et iusto odio dignissim qui blandit praesent luptatum zzril delenit augue duis dolore te feugait nulla facilisi.</p>
  </div>

  <aside class="abs news">
    <h2 class="display">Latest News</h2>
    <div class="news-item raised" style="top:51px">
      <div class="news-thumb" role="img" aria-label="Band members performing"></div>
      <div><div class="t">Lorem Ipsum Dolor</div><div class="d">Ut wisi enim ad minim veniam, quis nostrud exerci tation ullamcorper ....</div></div>
    </div>
    <div class="news-item" style="top:114px">
      <div class="news-thumb alt" role="img" aria-label="Band parade on a field"></div>
      <div><div class="t">Lorem Ipsum Dolor</div><div class="d">Ut wisi enim ad minim veniam, quis nostrud exerci tation ullamcorper ....</div></div>
    </div>
  </aside>

  <div class="abs rule"></div>

  <h2 class="abs cat-title display">Categories</h2>

  <div class="tile" style="left:171px;top:834px"><div class="pic" role="img" aria-label="Alto saxophone"></div><div class="name" style="bottom:0">Alto Sax</div></div>
  <div class="tile" style="left:345px;top:834px"><div class="pic" role="img" aria-label="Trumpet"></div><div class="name">Trumpet</div></div>
  <div class="tile active" style="left:518px;top:833px">
    <svg class="abs" style="left:72px;top:56px" width="22" height="22" viewBox="0 0 22 22"><circle cx="9" cy="9" r="7" fill="none" stroke="#fff" stroke-width="2.5"/><path d="m14 14 6 6M9 5v8M5 9h8" stroke="#fff" stroke-width="2.5"/></svg>
    <div class="label"><b>FLUTE</b><small>See All Products</small></div>
  </div>
  <div class="tile" style="left:693px;top:834px"><div class="pic dark" role="img" aria-label="Clarinets"></div><div class="name">Clarinet</div></div>
  <div class="tile" style="left:867px;top:834px"><div class="pic" role="img" aria-label="Trombone"></div><div class="name">Trombone</div></div>

  <div class="tile" style="left:171px;top:1023px"><div class="pic silver" role="img" aria-label="Tenor saxophone"></div><div class="name">Tenor Sax</div></div>
  <div class="tile" style="left:345px;top:1023px"><div class="pic silver" role="img" aria-label="Baritone horn"></div><div class="name">Baritone</div></div>
  <div class="tile" style="left:519px;top:1023px"><div class="pic" role="img" aria-label="Alto saxophone"></div><div class="name">Alto Sax</div></div>
  <div class="tile" style="left:693px;top:1023px"><div class="pic" role="img" aria-label="Trumpet"></div><div class="name">Trumpet</div></div>
  <div class="tile" style="left:867px;top:1023px"><div class="pic silver" role="img" aria-label="Flute"></div><div class="name">Flute</div></div>

  <div class="abs band"></div>
  <div class="abs band-arrow left"><svg width="12" height="10" viewBox="0 0 12 10"><path d="M0 5 5 0v3h7v4H5v3z" fill="var(--red)"/></svg></div>
  <div class="abs band-arrow right"><svg width="12" height="10" viewBox="0 0 12 10"><path d="M12 5 7 0v3H0v4h7v3z" fill="#fff"/></svg></div>

  <div class="card" style="left:170px"><h3>Rent-to-Own Musical Instruments</h3><div class="photo" role="img" aria-label="Marching band with red flags"></div></div>
  <div class="card" style="left:344px"><h3>Music Lessons in San Jose</h3><div class="photo" role="img" aria-label="Drum line students performing"></div></div>
  <div class="card active" style="left:518px"><h3>Guitars and Amps</h3>
    <div class="photo" role="img" aria-label="Acoustic guitar close-up"><svg width="24" height="24" viewBox="0 0 22 22"><circle cx="9" cy="9" r="7" fill="none" stroke="#fff" stroke-width="2.5"/><path d="m14 14 6 6M9 5v8M5 9h8" stroke="#fff" stroke-width="2.5"/></svg></div></div>
  <div class="card" style="left:692px"><h3>Band Instruments</h3><div class="photo" role="img" aria-label="Brass instruments on a red wall display"></div></div>
  <div class="card" style="left:866px"><h3>Drums and Percussion Instruments</h3><div class="photo" role="img" aria-label="Full marching band group on a field"></div></div>

  <footer>
    <p class="abs copy">Copyright © 2014 RIDGE HORN INSTRUMENTS. All Rights Reserved.</p>
    <div class="abs social" aria-label="Social links"><span></span><span></span><span></span><span></span></div>
  </footer>

</div>
</body>
</html>
```